artist "stamp" design

Im a young artist. I`m making a stamp with my information so i can make homemade business cards, so I need the following information to look good together and simple to read:

Lucila Marbán Oteiza

www.lumaroti.com

lucilamo47@vextramail.com

i want a very clan look, but with some personality. a simple logo or "look" would be great but nothing to fancy.

An idea I had was to make it look like it was written with a typewriter or a concept like that...be creative! thank you!
Updates

I don't want any image or icon, just letters, I need it to be compacto, I'm making a stamp

I don't want it to say photography 

I dont want my name to take over so it should stay close to the size as the rest of the info.

all my info should be included, this is not a logo its a design for a stamp meant to fin in a business card.

Target Market(s)

I'm a photographer, I want something very simple and I need this to make a stamp that ill use to pit on my cards and CV. I want something simple and modern

Industry/Entity Type

Business

Logo Text

Lucila Marbán Oteiza

Logo styles of interest
Abstract Logo
Wordmark Logo
Lettermark Logo
Font styles to use
Serif
Sans Serif

Requirements
Must have
• Has to look young and fresh
Nice to have
• Have to see how it looks on a business card with website and and email
Should not have
• Images

```html
<!DOCTYPE html>
<html lang="en">
<head>
<meta charset="UTF-8">
<title>Lucila Marbán Oteiza — Stamp</title>
<link href="https://fonts.googleapis.com/css2?family=Arvo&display=swap" rel="stylesheet">
<style>
  :root {
    --paper: #ffffff;
    --ink: #231f20;
  }
  html, body {
    margin: 0;
    padding: 0;
    width: 1200px;
    height: 1000px;
    overflow: hidden;
    background: var(--paper);
  }
  .canvas {
    position: relative;
    width: 1200px;
    height: 1000px;
    background: var(--paper);
  }
  .stamp-frame {
    position: absolute;
    left: 0;
    top: 0;
    width: 1200px;
    height: 1000px;
  }
  .stamp-frame path {
    fill: none;
    stroke: var(--ink);
    stroke-width: 4.5;
    stroke-linecap: butt;
    stroke-linejoin: miter;
  }
  .stamp-text {
    position: absolute;
    left: 143px;
    top: 0;
    margin: 0;
    font-family: "Arvo", "Rockwell", serif;
    color: var(--ink);
    white-space: nowrap;
    line-height: 1;
  }
  .stamp-name {
    top: 374px;
    font-size: 44px;
    letter-spacing: 5px;
  }
  .stamp-name .initial {
    font-size: 70px;
    letter-spacing: 3px;
  }
  .stamp-web {
    top: 476px;
    font-size: 44px;
    letter-spacing: 6px;
  }
  .stamp-mail {
    top: 562px;
    font-size: 44px;
    letter-spacing: 6px;
  }
</style>
</head>
<body>
<main class="canvas">
  <svg class="stamp-frame" viewBox="0 0 1200 1000" aria-hidden="true">
    <!-- top edge, with a small break near the left corner -->
    <path d="M143 325.5 L80.5 325.5 L81 673 L1118 673 L1118 606"/>
    <path d="M1118 578 L1117.5 325.5 L192 325"/>
  </svg>

  <p class="stamp-text stamp-name"><span class="initial">L</span>ucila <span class="initial">M</span>arbán <span class="initial">O</span>teiza</p>
  <p class="stamp-text stamp-web">www.lumaroti.com</p>
  <p class="stamp-text stamp-mail">lucilamo47@vextramail.com</p>
</main>
</body>
</html>
```